I need a business card design for a new company that will be doing consulting work around issues of cultural competency, and diversity and inclusion. I would like the design to be crisp and clear with bold but conservative colors and incorporate shades of blue

Target Market(s)

Small businesses, schools, non-profits

Industry/Entity Type

Consulting

Font styles to use
Serif
Sans Serif

Colors
0c5ba6
6b449b
3276b5
0292cd

Requirements
Must have
• A Morrow Venture (name of company)
• Lemlem Tavish
• CEO
• lemlem@amorrowventure.com
• (215)483-2756

```html
<!DOCTYPE html>
<html lang="en">
<head>
<meta charset="utf-8">
<title>A Morrow Venture – Business Card</title>
<link rel="stylesheet" href="https://fonts.googleapis.com/css2?family=Archivo:wght@800&family=Lexend:wght@200;300;400&display=swap">
<style>
  :root {
    --paper: #ffffff;
    --charcoal: #38383a;
    --ribbon-blue: #1591cd;
    --fold-blue-light: #3a86d4;
    --fold-blue-dark: #1f5fae;
    --ink-white: #ffffff;
  }
  html, body {
    margin: 0;
    padding: 0;
    overflow: hidden;
    background: var(--paper);
  }
  .card {
    position: relative;
    width: 1200px;
    height: 763px;
    background: var(--paper);
    overflow: hidden;
  }
  .card-shapes {
    position: absolute;
    inset: 0;
  }
  .charcoal-panel { fill: var(--charcoal); }
  .ribbon { fill: var(--ribbon-blue); }
  .ribbon-fold { fill: url(#foldShade); }

  .person-name,
  .person-title,
  .contact-phone,
  .contact-email,
  .company-name {
    position: absolute;
    margin: 0;
    white-space: nowrap;
    line-height: 1;
  }
  .person-name {
    left: 133px;
    top: 152px;
    font-family: "Lexend", sans-serif;
    font-weight: 400;
    font-size: 57px;
    color: var(--ink-white);
    letter-spacing: 0.5px;
  }
  .person-title {
    left: 133px;
    top: 214px;
    font-family: "Lexend", sans-serif;
    font-weight: 200;
    font-size: 50px;
    color: var(--charcoal);
  }
  .contact-phone {
    left: 131px;
    top: 480px;
    font-family: "Lexend", sans-serif;
    font-weight: 300;
    font-size: 42px;
    color: var(--charcoal);
  }
  .contact-email {
    left: 131px;
    top: 547px;
    font-family: "Lexend", sans-serif;
    font-weight: 300;
    font-size: 42px;
    color: var(--ink-white);
  }
  .company-name {
    right: 78px;
    top: 134px;
    text-align: right;
    font-family: "Archivo", sans-serif;
    font-weight: 800;
    font-size: 78px;
    line-height: 84px;
    color: var(--charcoal);
    letter-spacing: -0.5px;
  }
</style>
</head>
<body>
  <main class="card">
    <svg class="card-shapes" width="1200" height="763" viewBox="0 0 1200 763" aria-hidden="true">
      <defs>
        <linearGradient id="foldShade" x1="0" y1="0" x2="1" y2="1">
          <stop offset="0" stop-color="var(--fold-blue-light)"/>
          <stop offset="1" stop-color="var(--fold-blue-dark)"/>
        </linearGradient>
      </defs>
      <polygon class="charcoal-panel" points="38,38 501,38 847,728 38,728"/>

      <polygon class="ribbon-fold" points="628,282 672,282 641,311"/>
      <path class="ribbon" d="M117,136 H600 L672,282 H117 A26,26 0 0 1 91,256 V162 A26,26 0 0 1 117,136 Z"/>

      <polygon class="ribbon-fold" points="796,629 847,629 816,658"/>
      <path class="ribbon" d="M117,438 H751 L847,629 H117 A26,26 0 0 1 91,603 V464 A26,26 0 0 1 117,438 Z"/>
    </svg>

    <h1 class="person-name">Lemlem Tavish</h1>
    <p class="person-title">CEO</p>
    <p class="contact-phone">(215)483-2756</p>
    <p class="contact-email">lemlem@amorrowventure.com</p>
    <h2 class="company-name">A Morrow<br>Venture</h2>
  </main>
</body>
</html>
```